MODERN + COOL Business Card Needed!

SUMMARY
This is for a 40+ year old family business that is transitioning to the 2nd generation and is in real need of a more modern facelift. Ive attached a company logo (I made quickly as an idea with my limited PSD skills) to start off with that you are welcome to change and draw ideas from. Ive also attached some screen shots of cards I like to give you an idea of my preferences.

WHAT WE DO
The company name is Tall Pine HK Ltd. But I prefer to just call it Tall Pine or Tall Pine with Hong Kong as kind of a sub heading on the business card. We own a factory as well as help our customers find factories to make their product. Product I mean, toys 99.9% of the time. Simple old school toys like board games, puzzles, wooden toys, baby/infant toys.

You can say we are a "sourcing" or "trading" or "consulting" company with a factory to help you do it. But since we deal with toys, i like to keep it modern and cool and fun, not serious like managing hedge funds.

WHAT WE ARE LOOKING FOR
A cool, unique looking business card that stands out. In terms of design, something modern and professional. I like darker colored cards and I like colors such as blue/green/dark gray, but am open to other colored themes. I Like bright lime green with gray, always though thats a nice combo. I prefer cards that are all colored and not so much white showing (I think). Ive attached a few screenshots of cards so take a look to get a feel of what I like.

We do alot of wooden stacking games in variety of colors too like Tovra, Lumo, Towerplix (google these to check them out). So designs that sort of resemble stacking or building would be cool but totally not necessary.

In terms of the physical aspects of the card, Im looking for a card a bit different than the standard rectangular shape. Double sided. Little things like having corner(s) be round or different angle instead of square edge I always thought was nice. Its got to be mostly a normal card size, no folding or smaller cards that fit weird in your wallet. No vertical designs. Am open to VERY different/creative shapes (as long as it still fits in a wallet good like a normal buisness card.
Updates

Hi everyone!

Just wanted to write a message to everyone to let them know all submissions are being reviewed or have been reviewed.  If I have not responded with feedback, rest assure your submission was definitely looked at in detail but I either have just been too busy to respond (alot of submissions!), or its on my to be considered list.

I respect and really enjoy receiving everyones creativity and work so I dont want it to go unrecognized - thus this message!  Feel free to submit more ideas if you like until this project ends.  Sometimes some designs just dont click but sometimes they can so you never know!

Thanks again for everyones participation and great work!

~Dev Orr

Target Market(s)

The cards are mainly handed to toy company sourcers and buyers. People I talk to ... say Pelvane for example... might want to make their next edition of Farthingale game with a reputable factory at a good cost so they can sell it to stores at a profit.

So these are the types of people I often try to talk and introduce myself and my company to.

Industry/Entity Type

Building

Colors
acd036
0392cd
00a88e
474747
606060

Requirements
Must have
• Just double sided, not plain rectangle corners, and just cool to look at and catches your eye!

Oh and the obvious business card stuff like place for name, address, number, email, etc.
Nice to have
• Think more modern and fun, not serious and old fashion (thats what we used to be!). Can use the logo I attached and you can definitely alter and change the logo or make a whole new one!

Oh and can definitely use a creative slogan if you like to think of one based on what I described in what we do.
Should not have
• Dont use fonts or text placement that might make "Tall Pine" look like "Tal Lpine"... We arent selling news papers!!

Please nothing related to education since we have the word Pine in the title, thats not our business at all.

Logo and design should not be too heavy on things related to toys, as though thats what we primarily focus on now, what we do may change over time.

```html
<!DOCTYPE html>
<html lang="en">
<head>
<meta charset="utf-8">
<title>Tall Pine – Business Card</title>
<link rel="stylesheet" href="https://fonts.googleapis.com/css2?family=Arimo:wght@400;700&display=swap">
<style>
  :root {
    --stage: #1c1b1c;
    --card-dark: #231f20;
    --card-gray: #59595b;
    --brand-teal: #1aa3b5;
    --sub-gray: #5a5a5c;
    --ink-white: #ffffff;
    --ink-dark: #262626;
    --edge: #d8d8d8;
  }
  * { box-sizing: border-box; margin: 0; padding: 0; }
  html, body {
    width: 1200px; height: 900px; overflow: hidden;
    background: var(--stage);
    font-family: "Arimo", Arial, sans-serif;
  }
  .canvas { position: relative; width: 1200px; height: 900px; }

  .card {
    position: absolute;
    border-radius: 24px;
    overflow: hidden;
    border: 2px solid var(--edge);
  }
  .card--front {
    left: 134px; top: 30px; width: 646px; height: 403px;
    background: var(--card-gray);
  }
  .card--back {
    left: 413px; top: 472px; width: 646px; height: 401px;
    background: var(--card-dark);
  }

  .front__band {
    position: absolute; left: 0; top: 0; width: 100%; height: 135px;
    background: var(--card-dark);
  }

  .brand {
    position: absolute;
    display: flex; flex-direction: column; align-items: flex-end;
  }
  .brand__name {
    display: flex; align-items: center; gap: 16px;
    font-weight: 700; font-size: 60px; line-height: 1;
    letter-spacing: 2px;
    color: var(--brand-teal);
    white-space: nowrap;
  }
  .brand__mark {
    display: inline-block; width: 44px; height: 44px;
    background: var(--brand-teal);
    border-radius: 6px;
  }
  .brand__sub {
    margin-top: 4px;
    font-size: 15px; font-weight: 400;
    letter-spacing: 9px;
    color: var(--sub-gray);
    white-space: nowrap;
    margin-right: -9px;
  }
  .front__brand { left: 96px; top: 40px; }
  .back__brand { left: 106px; top: 158px; }

  .holder-name {
    position: absolute; left: 76px; top: 183px;
    font-size: 40px; font-weight: 700; color: var(--ink-white);
  }
  .contact-list {
    position: absolute; left: 76px; top: 258px;
    list-style: none;
    font-size: 17px; color: var(--ink-dark);
    line-height: 24px;
  }
  .contact-list li { display: flex; align-items: center; gap: 4px; }
  .contact-list svg { width: 16px; height: 16px; fill: var(--ink-dark); flex: none; }
</style>
</head>
<body>
<main class="canvas">

  <section class="card card--front" aria-label="Card front">
    <div class="front__band"></div>
    <div class="brand front__brand">
      <div class="brand__name"><span class="brand__mark"></span>Tall Pine</div>
      <div class="brand__sub">HONG KONG</div>
    </div>
    <h1 class="holder-name">Dev Orr</h1>
    <ul class="contact-list">
      <li>
        <svg viewBox="0 0 16 16" aria-hidden="true"><path d="M4 1l3 3-2 2c1 2 3 4 5 5l2-2 3 3-2 2C7 15 1 9 2 3z"/></svg>
        Phone
      </li>
      <li>
        <svg viewBox="0 0 16 16" aria-hidden="true"><path d="M5 1h6v14H5zM6 3v8h4V3z"/></svg>
        Mobile
      </li>
      <li>
        <svg viewBox="0 0 16 16" aria-hidden="true"><path d="M1 4h14v9H1zM2 5l6 5 6-5v-.5H2z"/></svg>
        email
      </li>
      <li>
        <svg viewBox="0 0 16 16" aria-hidden="true"><circle cx="8" cy="8" r="7"/><path d="M1 8h14M8 1c-3 4-3 10 0 14M8 1c3 4 3 10 0 14" stroke="#59595b" stroke-width="1" fill="none"/></svg>
        website
      </li>
    </ul>
  </section>

  <section class="card card--back" aria-label="Card back">
    <div class="brand back__brand">
      <div class="brand__name"><span class="brand__mark"></span>Tall Pine</div>
      <div class="brand__sub">HONG KONG</div>
    </div>
  </section>

</main>
</body>
</html>
```